Ashcombe Field Surveyors Business Card

We are a land surveying company looking for a business card with a clean, sharp design. We would like for our design to portray our logo on one side, and contact information on the other w/ or w/o logo. Our colors preferred are navy blue, grey/silver, white and black. thank you!

Industry/Entity Type

Surveyor

Contact Information for Business Card

Ashcombe Field Surveyors
Dorian Kavatsky, P.L.S.
(555) 302-4619
Ashcombefieldsurveyors@ashmail-example.net
Ashcombefieldsurveyors-example.com
287 Linden Terrace, Alderbrook MA 01999

Requirements
Must have
• 1. Company Name
2. Personal name and title
3. phone number
4. email.
5. website
6. address

```html
<!DOCTYPE html>
<html lang="en">
<head>
<meta charset="utf-8">
<title>Ashcombe Field Surveyors – Business Card</title>
<link href="https://fonts.googleapis.com/css2?family=Montserrat:wght@600;700&family=Roboto:wght@400&display=swap" rel="stylesheet">
<style>
  :root {
    --navy: #2e3692;
    --paper: #ffffff;
    --backdrop: #8c8c8c;
    --ink: #4a4a4a;
    --rule: #6b6b6b;
  }
  * { box-sizing: border-box; margin: 0; padding: 0; }
  html, body { width: 1200px; height: 1118px; overflow: hidden; }
  body {
    background: var(--backdrop);
    position: relative;
    font-family: "Roboto", sans-serif;
  }
  .card {
    position: absolute;
    left: 250px;
    width: 700px;
    height: 400px;
    overflow: hidden;
    box-shadow: 0 12px 30px rgba(0,0,0,0.35);
  }
  .card--front { top: 110px; background: var(--navy); }
  .card--back { top: 600px; background: var(--paper); }

  .front-mark {
    position: absolute;
    left: 40px; top: 60px;
    width: 230px; height: 230px;
    border: 5px solid var(--paper);
    border-radius: 50%;
  }
  .front-name {
    position: absolute;
    left: 310px; top: 140px;
    color: var(--paper);
    font-family: "Montserrat", sans-serif;
    font-weight: 600;
    font-size: 34px;
    letter-spacing: 3px;
    line-height: 1.25;
    text-transform: uppercase;
  }

  .back-name-block {
    position: absolute;
    right: 50px; top: 50px;
    text-align: right;
    color: var(--navy);
    font-family: "Montserrat", sans-serif;
    font-weight: 600;
    font-size: 26px;
    letter-spacing: 2px;
    line-height: 1.25;
    text-transform: uppercase;
  }
  .rule {
    position: absolute;
    left: 50px; right: 50px; top: 160px;
    border-top: 1px solid var(--rule);
  }
  .person {
    position: absolute;
    left: 50px; top: 188px;
    color: var(--navy);
    font-family: "Montserrat", sans-serif;
    font-weight: 700;
    font-size: 24px;
    letter-spacing: 0.5px;
  }
  .person-rule {
    position: absolute;
    left: 50px; top: 226px; width: 340px;
    border-top: 1px solid var(--rule);
  }
  .contacts {
    position: absolute;
    left: 50px; top: 240px;
    list-style: none;
    color: var(--ink);
    font-size: 16px;
  }
  .contacts li {
    display: flex; align-items: center; gap: 10px;
    height: 30px;
  }
  .contacts svg, .address svg { width: 18px; height: 18px; fill: var(--navy); flex: none; }
  .address {
    position: absolute;
    right: 50px; top: 240px;
    display: flex; gap: 10px;
    color: var(--ink);
    font-size: 16px;
    line-height: 1.4;
  }
  .band {
    position: absolute;
    left: 0; right: 0; bottom: 0; height: 34px;
    background: var(--navy);
  }
</style>
</head>
<body>
  <section class="card card--front">
    <div class="front-mark"></div>
    <h1 class="front-name">Ashcombe<br>Field Surveyors</h1>
  </section>

  <section class="card card--back">
    <div class="back-name-block">Ashcombe<br>Field Surveyors</div>
    <div class="rule"></div>
    <h2 class="person">DORIAN KAVATSKY, P.L.S.</h2>
    <div class="person-rule"></div>
    <ul class="contacts">
      <li>
        <svg viewBox="0 0 24 24" aria-hidden="true"><path d="M6.6 10.8a15.1 15.1 0 0 0 6.6 6.6l2.2-2.2c.3-.3.7-.4 1-.2 1.1.4 2.3.6 3.6.6.6 0 1 .4 1 1V20c0 .6-.4 1-1 1C10.6 21 3 13.4 3 4c0-.6.4-1 1-1h3.5c.6 0 1 .4 1 1 0 1.3.2 2.5.6 3.6.1.3 0 .7-.2 1L6.6 10.8z"/></svg>
        (555) 302-4619
      </li>
      <li>
        <svg viewBox="0 0 24 24" aria-hidden="true"><path d="M2 5h20v14H2V5zm2 2v.5l8 5 8-5V7H4zm16 2.8-8 5-8-5V17h16V9.8z"/></svg>
        Ashcombefieldsurveyors@ashmail-example.net
      </li>
      <li>
        <svg viewBox="0 0 24 24" aria-hidden="true"><path d="M12 2a10 10 0 1 0 0 20 10 10 0 0 0 0-20zm6.9 6h-3a15.7 15.7 0 0 0-1.3-3.9A8 8 0 0 1 18.9 8zM12 4c.8 1.2 1.5 2.5 1.9 4h-3.8c.4-1.5 1.1-2.8 1.9-4zM4.3 14a8.2 8.2 0 0 1 0-4h3.4a16.5 16.5 0 0 0 0 4H4.3zm.8 2h3a15.7 15.7 0 0 0 1.3 3.9A8 8 0 0 1 5.1 16zm3-8h-3a8 8 0 0 1 4.3-3.9C8.8 5.3 8.4 6.6 8.1 8zM12 20c-.8-1.2-1.5-2.5-1.9-4h3.8c-.4 1.5-1.1 2.8-1.9 4zm2.3-6H9.7a14.7 14.7 0 0 1 0-4h4.6a14.7 14.7 0 0 1 0 4zm.3 5.9c.6-1.2 1-2.5 1.3-3.9h3a8 8 0 0 1-4.3 3.9zm1.7-5.9a16.5 16.5 0 0 0 0-4h3.4a8.2 8.2 0 0 1 0 4h-3.4z"/></svg>
        www.Ashcombefieldsurveyors-example.com
      </li>
    </ul>
    <div class="address">
      <svg viewBox="0 0 24 24" aria-hidden="true"><path d="M12 2a7 7 0 0 0-7 7c0 5.2 7 13 7 13s7-7.8 7-13a7 7 0 0 0-7-7zm0 9.5a2.5 2.5 0 1 1 0-5 2.5 2.5 0 0 1 0 5z"/></svg>
      <span>287 Linden Terrace,<br>Alderbrook MA 01999</span>
    </div>
    <div class="band"></div>
  </section>
</body>
</html>
```